Christmas Concert

"The Ashcombe Voices" is Thornwick Manor's professional chamber choir. www.ashcombevoices-example.com

They are performing a Christmas concert in Oxford's oldest building, St Aldric by the Westmarch (almost 1,000 years old), and the concert will be by candlelight.

We are looking for a dramatic and sophisticated Christmas poster that will stand out in the crowd of other posters in Oxford city centre.

We are thinking of calling the concert "Christmas with the Ashcombe Voices" or "Christmas Carols by Candlelight" but we're open to suggestions.

The poster will be used for digital dissemination (as well as Chatterly/Quipster) as well as print - A2 (portrait) will be the maximum size.

See attached photo of the ensemble. It would be a good to incorporate this in some way.
Updates

Industry/Entity Type

Building

Requirements
Nice to have
• The Ashcombe Voices
• Neil Carrow-Pritchard, Director
• Sunday 8 December
• 8pm
• Tickets £10/£5
• AshcombeVoices-example.com

```html
<!DOCTYPE html>
<html lang="en">
<head>
<meta charset="utf-8">
<title>Christmas Carols by Candlelight</title>
<link rel="stylesheet" href="https://fonts.googleapis.com/css2?family=Pinyon+Script&family=Libre+Baskerville:wght@400;700&family=Playfair+Display:wght@700;900&display=swap">
<style>
  :root {
    --night: #0b0a14;
    --deep-red: #3a0306;
    --crimson: #8e0b12;
    --scarlet: #b5141b;
    --gold: #e8b25a;
    --stone: #a77a45;
    --white: #ffffff;
    --cream: #fbf1e2;
  }
  * { margin: 0; padding: 0; box-sizing: border-box; }
  html, body { width: 849px; height: 1200px; overflow: hidden; background: var(--night); }
  .poster {
    position: relative;
    width: 849px;
    height: 1200px;
    overflow: hidden;
    background:
      radial-gradient(ellipse 70% 40% at 50% 62%, var(--scarlet) 0%, rgba(181,20,27,0) 70%),
      linear-gradient(180deg, var(--night) 0%, var(--deep-red) 45%, var(--crimson) 70%, var(--deep-red) 100%);
    color: var(--white);
    text-align: center;
  }
  .ensemble-photo {
    position: absolute;
    left: 0; top: 0;
    width: 849px; height: 600px;
    background:
      radial-gradient(ellipse 45% 30% at 50% 22%, rgba(232,178,90,0.55) 0%, rgba(232,178,90,0) 70%),
      radial-gradient(ellipse 60% 25% at 50% 75%, rgba(40,20,20,0.9) 0%, rgba(40,20,20,0) 80%),
      linear-gradient(180deg, #07070d 0%, #2a2118 18%, var(--stone) 30%, #5a3a1e 45%, #1c0f0c 70%, rgba(58,3,6,0) 100%);
  }
  .candles {
    position: absolute;
    top: 880px;
    width: 300px; height: 300px;
  }
  .candles--left {
    left: 0;
    background: radial-gradient(ellipse 80% 60% at 20% 55%, rgba(255,190,110,0.55) 0%, rgba(142,11,18,0.4) 45%, rgba(58,3,6,0) 80%);
  }
  .candles--right {
    right: 0;
    background: radial-gradient(ellipse 80% 60% at 80% 55%, rgba(255,190,110,0.55) 0%, rgba(142,11,18,0.4) 45%, rgba(58,3,6,0) 80%);
  }
  .title {
    font-family: "Pinyon Script", cursive;
    font-weight: 400;
    text-shadow: 0 3px 12px rgba(0,0,0,0.6);
  }
  .title span {
    position: absolute;
    left: 0; right: 0;
    display: block;
    white-space: nowrap;
  }
  .title__main { top: 440px; font-size: 150px; line-height: 150px; }
  .title__carols { top: 588px; font-size: 108px; line-height: 108px; }
  .title__candle { top: 690px; font-size: 104px; line-height: 108px; }
  .intro {
    position: absolute;
    left: 120px; right: 120px; top: 818px;
    font-family: "Libre Baskerville", serif;
    font-size: 17px;
    line-height: 24px;
    color: var(--cream);
  }
  .date {
    position: absolute;
    left: 0; right: 0; top: 930px;
    font-family: "Playfair Display", serif;
    font-weight: 900;
  }
  .date__day { display: block; font-size: 50px; line-height: 54px; letter-spacing: 1px; }
  .date__full { display: block; font-size: 40px; line-height: 48px; }
  .date__full sup { font-size: 22px; }
  .venue {
    position: absolute;
    left: 0; right: 0; top: 1044px;
    font-family: "Libre Baskerville", serif;
    font-size: 20px;
    line-height: 32px;
  }
  .venue__tickets { font-size: 23px; }
  .website {
    position: absolute;
    left: 0; right: 0; top: 1140px;
    font-family: "Libre Baskerville", serif;
    font-weight: 700;
    font-size: 21px;
    line-height: 30px;
    letter-spacing: 0.5px;
  }
</style>
</head>
<body>
<main class="poster">
  <div class="ensemble-photo" role="img" aria-label="Photograph of the choir in evening dress standing before a floodlit stately manor at night, lit by rows of candles"></div>
  <div class="candles candles--left" role="img" aria-label="Glowing red pillar candles"></div>
  <div class="candles candles--right" role="img" aria-label="Glowing red pillar candles"></div>

  <h1 class="title">
    <span class="title__main">Christmas</span>
    <span class="title__carols">Carols</span>
    <span class="title__candle">by Candlelight</span>
  </h1>

  <p class="intro">The Ashcombe Voices and Vocalensemble Brevio present a festive programme of your favourite Christmas carols and songs in Oxford's oldest building by candlelight. The evening will include audience carols and mulled wine served at the interval.</p>

  <p class="date">
    <span class="date__day">SUNDAY</span>
    <span class="date__full">8<sup>th</sup> DECEMBER, 2013 8 PM</span>
  </p>

  <p class="venue">
    St Aldric by the Westmarch, Harrowgate Lane, Oxford, OX9 4ZZ<br>
    <span class="venue__tickets">Tickets £10/£5 on the door</span>
  </p>

  <p class="website">www.ashcombevoices-example.com</p>
</main>
</body>
</html>
```